iOS App Design Project for Pebble Notes

We are looking for a redesign of the UI for our app, Pebble Notes. The app is a to-do list type app with 4 screens, and we already have a UI for it but we would like a nicer looking one that has a better colour scheme and is more intuitive.

We would like something that is a real treat to look at, and that users really want to use. Essentially what we want is the nicest and most simple design possible, as the current UI we have is not very user friendly.

The app is already on the market and is free so if you have an iOS device you can download it and take a look at it, and we have also included screenshots of the app.
Updates

Project Deadline Extended
Reason: I am updating the design brief and will also guarantee the payment.

Target Market(s)

Mobile users looking for simplicity

Requirements
Must have
• - Very visually pleasing
- Simple layout with minimal clutter
- Icons and buttons that explain what they do
Should not have
• Any features that detract from the simplicity of the app are not wanted.

```html
<!DOCTYPE html>
<html lang="en">
<head>
<meta charset="utf-8">
<title>Pebble Notes – Task</title>
<link rel="stylesheet" href="https://fonts.googleapis.com/css2?family=Source+Sans+3:wght@400;600;700&family=Arimo:wght@400;700&display=swap">
<style>
  :root{
    --status-bg:#000;
    --nav-top:#3c75ad;
    --nav-bottom:#1d4f86;
    --paper:#f2eee6;
    --paper-dark:#e6dfd2;
    --popover-top:#b3c3d3;
    --popover-bottom:#8fa2b4;
    --popover-text:#545b63;
    --green-top:#1e9a48;
    --green-bottom:#0b6d2d;
    --red-top:#c9474a;
    --red-bottom:#9b1f23;
    --red-icon:#5e1517;
    --blue-swatch:#1a9be0;
    --orange-swatch:#fb6a3f;
    --green-swatch:#5bb850;
    --yellow-swatch:#fbeb5b;
    --gray-swatch:#777;
    --button-light:#e4e4e4;
    --button-mid:#c6c6c6;
    --ad-bg:#2e2e2e;
    --tab-top:#2f6aa3;
    --tab-bottom:#1a4b80;
    --tab-active:#0e3459;
    --white:#fff;
  }
  *{box-sizing:border-box;margin:0;padding:0}
  html,body{width:800px;height:1200px;overflow:hidden;background:var(--paper)}
  body{position:relative;font-family:"Source Sans 3",sans-serif}

  .status-bar{position:absolute;left:0;top:0;width:800px;height:50px;background:var(--status-bg);color:var(--white);font-family:"Arimo",sans-serif;font-weight:700;font-size:28px}
  .status-bar .carrier{position:absolute;left:10px;top:8px;display:flex;align-items:center;gap:8px}
  .status-bar .clock{position:absolute;left:0;right:0;top:8px;text-align:center}
  .status-bar .battery{position:absolute;right:12px;top:8px;display:flex;align-items:center;gap:8px}

  .nav-bar{position:absolute;left:0;top:50px;width:800px;height:110px;background:linear-gradient(var(--nav-top),var(--nav-bottom));border-bottom:2px solid #15406e;display:flex;align-items:center;justify-content:center}
  .nav-title{color:var(--white);font-size:56px;font-weight:400;text-shadow:0 -2px 0 rgba(0,0,0,.35)}

  .content{position:absolute;left:0;top:160px;width:800px;height:795px;background:linear-gradient(var(--paper),var(--paper-dark))}

  .btn{position:absolute;border-radius:6px;display:flex;align-items:center;justify-content:center;box-shadow:0 2px 3px rgba(0,0,0,.35)}
  .btn-done{left:69px;top:204px;width:112px;height:66px;background:linear-gradient(var(--green-top),var(--green-bottom))}
  .btn-info{left:660px;top:204px;width:79px;height:66px;background:linear-gradient(var(--button-light),var(--button-mid))}
  .btn-add{left:334px;top:788px;width:129px;height:127px;border-radius:8px;background:linear-gradient(var(--red-top),var(--red-bottom))}

  .mode-toggle{position:absolute;left:423px;top:203px;width:187px;height:70px;border-radius:8px;overflow:hidden;display:flex;box-shadow:0 2px 3px rgba(0,0,0,.35)}
  .mode-color{width:112px;background:linear-gradient(var(--button-light),var(--button-mid));display:flex;align-items:center;justify-content:center}
  .mode-color span{width:68px;height:40px;border-radius:8px;background:var(--blue-swatch)}
  .mode-tag{flex:1;background:linear-gradient(#8a8481,#6f6a68);display:flex;align-items:center;justify-content:center;box-shadow:inset 0 2px 5px rgba(0,0,0,.4)}

  .color-popover{position:absolute;left:69px;top:335px;width:662px;height:263px;border-radius:12px;background:linear-gradient(var(--popover-top),var(--popover-bottom));box-shadow:0 3px 4px rgba(0,0,0,.3)}
  .popover-arrow{position:absolute;left:371px;top:-46px}
  .popover-label{position:absolute;left:0;right:0;top:52px;text-align:center;color:var(--popover-text);font-size:33px}
  .swatches{position:absolute;left:30px;top:140px;display:flex;gap:31px}
  .swatch{width:94px;height:58px;border-radius:12px;border:1px solid rgba(0,0,0,.3);box-shadow:inset 0 14px 0 rgba(255,255,255,.12),0 1px 2px rgba(0,0,0,.25)}
  .swatch.blue{background:var(--blue-swatch)}
  .swatch.orange{background:var(--orange-swatch)}
  .swatch.green{background:var(--green-swatch)}
  .swatch.yellow{background:var(--yellow-swatch)}
  .swatch.gray{background:var(--gray-swatch)}

  .ad-band{position:absolute;left:0;top:955px;width:800px;height:123px;background:var(--ad-bg);display:flex;align-items:center;justify-content:center;color:var(--white);font-family:"Arimo",sans-serif;font-size:32px}

  .tab-bar{position:absolute;left:0;top:1078px;width:800px;height:122px;background:linear-gradient(var(--tab-top),var(--tab-bottom))}
  .tab{position:absolute;top:12px;width:160px;display:flex;flex-direction:column;align-items:center;color:var(--white);font-weight:700;font-size:28px}
  .tab svg{height:66px;margin-bottom:4px}
  .tab.active{color:var(--tab-active)}
  .tab-list{left:13px}.tab-task{left:210px}.tab-notes{left:422px}.tab-more{left:622px}
</style>
</head>
<body>
  <header class="status-bar">
    <div class="carrier">
      <svg width="34" height="20" viewBox="0 0 34 20"><rect x="0" y="14" width="5" height="6" fill="#fff"/><rect x="7" y="11" width="5" height="9" fill="#fff"/><rect x="14" y="8" width="5" height="12" fill="#fff"/><rect x="21" y="4" width="5" height="16" fill="#777"/><rect x="28" y="0" width="5" height="20" fill="#777"/></svg>
      <span>Nimbus</span>
      <svg width="30" height="22" viewBox="0 0 30 22"><path d="M15 21 L3 8 A17 17 0 0 1 27 8 Z" fill="#fff"/></svg>
    </div>
    <div class="clock">7:29 PM</div>
    <div class="battery">
      <svg width="22" height="22" viewBox="0 0 22 22"><path d="M21 1 L1 10 L11 11 L12 21 Z" fill="#fff"/></svg>
      <span>30%</span>
      <svg width="44" height="22" viewBox="0 0 44 22"><rect x="1" y="1" width="38" height="20" rx="3" fill="none" stroke="#fff" stroke-width="2"/><rect x="4" y="4" width="11" height="14" fill="#fff"/><rect x="40" y="7" width="3" height="8" fill="#fff"/></svg>
    </div>
  </header>

  <nav class="nav-bar"><h1 class="nav-title">Hello 2</h1></nav>

  <main class="content"></main>

  <div class="btn btn-done" aria-label="Mark done">
    <svg width="50" height="46" viewBox="0 0 50 46"><path d="M4 26 Q10 22 16 32 Q28 8 46 2 Q30 16 18 44 Q12 32 4 26 Z" fill="#0b2a14"/></svg>
  </div>

  <div class="mode-toggle" aria-label="Color or tag mode">
    <div class="mode-color"><span></span></div>
    <div class="mode-tag">
      <svg width="50" height="40" viewBox="0 0 50 40"><path d="M4 20 L22 4 H44 V36 H22 Z" fill="none" stroke="#3e3a38" stroke-width="4" stroke-linejoin="round" transform="rotate(-30 25 20) translate(6 0)"/><circle cx="36" cy="13" r="3" fill="#3e3a38"/></svg>
    </div>
  </div>

  <div class="btn btn-info" aria-label="Info">
    <svg width="44" height="44" viewBox="0 0 44 44"><circle cx="22" cy="22" r="20" fill="#555"/><circle cx="22" cy="12" r="3.5" fill="#e4e4e4"/><rect x="18.5" y="18" width="7" height="16" rx="1" fill="#e4e4e4"/></svg>
  </div>

  <section class="color-popover">
    <svg class="popover-arrow" width="84" height="48" viewBox="0 0 84 48"><path d="M0 48 L42 2 L84 48 Z" fill="var(--popover-top)"/></svg>
    <p class="popover-label">Pick a color:</p>
    <div class="swatches">
      <span class="swatch blue"></span>
      <span class="swatch orange"></span>
      <span class="swatch green"></span>
      <span class="swatch yellow"></span>
      <span class="swatch gray"></span>
    </div>
  </section>

  <div class="btn btn-add" aria-label="Add task">
    <svg width="72" height="72" viewBox="0 0 72 72"><path d="M27 4 H45 V27 H68 V45 H45 V68 H27 V45 H4 V27 H27 Z" fill="var(--red-icon)" rx="3"/></svg>
  </div>

  <div class="ad-band">Advertising</div>

  <footer class="tab-bar">
    <div class="tab tab-list">
      <svg viewBox="0 0 60 66" width="60"><g fill="none" stroke="#fff" stroke-width="4"><path d="M2 8 L8 14 L18 2"/><rect x="4" y="28" width="12" height="12"/><rect x="4" y="50" width="12" height="12"/><path d="M24 12 H58 M24 34 H58 M24 56 H58"/></g></svg>
      <span>List</span>
    </div>
    <div class="tab tab-task active">
      <svg viewBox="0 0 66 66" width="66"><g fill="none" stroke="#0e3459" stroke-width="5"><rect x="5" y="10" width="56" height="52" rx="4"/><path d="M18 4 V16 M48 4 V16"/><path d="M18 36 L29 47 L49 25"/></g></svg>
      <span>Task</span>
    </div>
    <div class="tab tab-notes">
      <svg viewBox="0 0 64 66" width="64"><g fill="none" stroke="#fff" stroke-width="3.5"><path d="M4 4 H36 L46 14 V62 H4 Z"/><path d="M12 22 H38 M12 32 H38 M12 42 H38 M12 52 H38"/><path d="M54 8 V56 L57 62 L60 56 V8 Z"/></g></svg>
      <span>Notes</span>
    </div>
    <div class="tab tab-more">
      <svg viewBox="0 0 66 66" width="66"><circle cx="33" cy="33" r="31" fill="#fff"/><path d="M33 16 V50 M16 33 H50" stroke="#1d4f86" stroke-width="7"/></svg>
      <span>More</span>
    </div>
  </footer>
</body>
</html>
```